Wine label refresh

We are wanting to modify our Corran Estate label to include a picture on it.
I have attached the pictures below which we would like on the label. They are of the Corran Estate vineyard. I have also attached an example of another label with a picture on it that we like the style of.
Industry/Entity Type
Vineyard
Requirements
Must have
- The Corran Estate text must stay the same but can be moved down. It still needs to be the same size though.
Marlborough Sauvignon Blanc should remain in the same font and roughly the same size.
Wine of New Zealand also must stay but could potentially be moved.
Nice to have
- It would be nice if we could keep the KL logo on the front label but feel free to experiment with where this goes.

```html
<!DOCTYPE html>
<html lang="en">
<head>
<meta charset="utf-8">
<title>Corran Estate – Marlborough Sauvignon Blanc Label</title>
<link rel="stylesheet" href="https://fonts.googleapis.com/css2?family=Cinzel:wght@400&family=Pinyon+Script&family=Josefin+Sans:wght@300&display=swap">
<style>
  :root {
    --backdrop: #f3f1ec;
    --paper: #ffffff;
    --gold-dark: #b9845f;
    --gold-mid: #e3b898;
    --gold-light: #fbe8da;
    --ink-maroon: #7a1d2a;
    --ink-red: #c0182b;
    --ink-grey: #9a9a9a;
    --ink-origin: #6e6e6e;
    --photo-green: #4a7a38;
    --photo-green-soft: #5d8c49;
  }
  * { box-sizing: border-box; margin: 0; padding: 0; }
  html, body {
    width: 1200px;
    height: 1000px;
    overflow: hidden;
    background: var(--backdrop);
  }
  .canvas {
    position: relative;
    width: 1200px;
    height: 1000px;
  }
  .wine-label {
    position: absolute;
    left: 210px;
    top: 105px;
    width: 780px;
    height: 790px;
    background: var(--paper);
    padding: 22px 18px;
    box-shadow: 0 0 0 1px #e6e2dc;
  }
  .foil-band {
    height: 24px;
    background: linear-gradient(90deg,
      var(--gold-dark) 0%, var(--gold-mid) 18%, var(--gold-light) 30%,
      var(--gold-mid) 42%, var(--gold-dark) 55%, var(--gold-mid) 70%,
      var(--gold-light) 82%, var(--gold-dark) 100%);
  }
  .frame {
    position: relative;
    height: calc(100% - 48px);
    margin: 0 12px;
    border-left: 5px solid var(--gold-mid);
    border-right: 5px solid var(--gold-mid);
    display: flex;
    flex-direction: column;
    align-items: center;
  }
  .monogram {
    margin-top: 92px;
    font-family: "Cinzel", serif;
    font-weight: 400;
    font-size: 64px;
    line-height: 1;
    letter-spacing: 4px;
    color: var(--ink-maroon);
  }
  .estate-name {
    margin-top: 18px;
    font-family: "Cinzel", serif;
    font-weight: 400;
    font-size: 44px;
    letter-spacing: 2px;
    color: var(--ink-maroon);
  }
  .vineyard-photo {
    margin-top: 24px;
    width: 420px;
    height: 210px;
    border-radius: 50%;
    background: radial-gradient(ellipse at center, var(--photo-green-soft) 0%, var(--photo-green) 100%);
  }
  .varietal {
    margin-top: 26px;
    font-family: "Pinyon Script", cursive;
    font-size: 50px;
    line-height: 1;
    color: var(--ink-red);
  }
  .vintage {
    margin-top: 4px;
    font-family: "Pinyon Script", cursive;
    font-size: 46px;
    line-height: 1;
    color: var(--ink-red);
  }
  .statutory {
    position: absolute;
    bottom: 18px;
    left: 0;
    right: 0;
    display: flex;
    justify-content: space-between;
    padding: 0 24px;
    font-family: "Josefin Sans", sans-serif;
    font-weight: 300;
    font-size: 19px;
    letter-spacing: 1px;
    color: var(--ink-grey);
  }
  .statutory .origin { color: var(--ink-origin); }
</style>
</head>
<body>
  <main class="canvas">
    <section class="wine-label">
      <div class="foil-band"></div>
      <div class="frame">
        <div class="monogram">KL</div>
        <h1 class="estate-name">CORRAN ESTATE</h1>
        <div class="vineyard-photo" role="img" aria-label="Photograph of the Corran Estate vineyard"></div>
        <p class="varietal">Marlborough Sauvignon Blanc</p>
        <p class="vintage">2012</p>
        <p class="statutory">
          <span class="volume">750ML</span>
          <span class="origin">PRODUCE OF NEW ZEALAND</span>
          <span class="alcohol">13% VOL</span>
        </p>
      </div>
      <div class="foil-band"></div>
    </section>
  </main>
</body>
</html>
```